Freelance business trainer needs a new business card

My business is called Tbrite. I provide training in the workplace on management, coaching and mentoring, and customer service topics for a variety of businesses, colleges and private training providers, and teach on management programs. I need a professional but eye catching business card. Business colours grey and orange. My name Linda Marchbank; Tel 07853 416207; email lmarchbank@tbrite.co.uk; website www.tbrite.co.uk.
Happy to have some sort of logo on front and details on back or all on one side
Target Market(s)
SME businesses and colleges - workshops i run are for adults in the workplace
Industry/Entity Type
Training
Look and feel

```html
<!DOCTYPE html>
<html lang="en">
<head>
<meta charset="utf-8">
<title>Tbrite – Business Card</title>
<link rel="stylesheet" href="https://fonts.googleapis.com/css2?family=Questrial&display=swap">
<style>
  :root {
    --orange: #f7901e;
    --charcoal: #4a4a4c;
    --band-grey: #d6d6d6;
    --text-grey: #4d4d4d;
    --white: #ffffff;
    --backdrop: #ececec;
    --font: "Questrial", "Century Gothic", sans-serif;
  }
  * { box-sizing: border-box; margin: 0; padding: 0; }
  html, body { width: 1200px; height: 711px; overflow: hidden; }
  body {
    background: var(--backdrop);
    font-family: var(--font);
    position: relative;
  }
  .card {
    position: absolute;
    top: 75px;
    width: 340px;
    height: 560px;
    border-radius: 24px;
    overflow: hidden;
    box-shadow: 0 6px 18px rgba(0,0,0,0.18);
  }

  /* Front */
  .card--front { left: 230px; background: var(--orange); }
  .front-band {
    position: absolute;
    left: 0; right: 0;
    top: 190px; height: 120px;
    background: var(--charcoal);
    display: flex; flex-direction: column;
    align-items: center; justify-content: center;
  }
  .brand-name {
    color: var(--orange);
    font-size: 56px;
    line-height: 1;
    letter-spacing: 1px;
  }
  .brand-tagline {
    color: var(--white);
    font-size: 11.5px;
    margin-top: 6px;
    letter-spacing: 0.2px;
  }

  /* Back */
  .card--back { left: 630px; background: var(--white); }
  .back-logo-panel {
    position: absolute;
    left: 20px; top: 18px;
    width: 300px; height: 170px;
    background: var(--charcoal);
    border-radius: 14px;
    display: flex; flex-direction: column;
    align-items: center; justify-content: center;
  }
  .back-logo-panel .brand-name { font-size: 66px; }
  .back-logo-panel .brand-tagline { font-size: 12.5px; margin-top: 8px; }

  .name-band {
    position: absolute;
    left: 0; right: 0;
    top: 210px; height: 48px;
    background: var(--band-grey);
  }
  .person-name {
    position: absolute;
    left: 24px; top: 217px;
    color: var(--orange);
    font-size: 29px;
    font-weight: 400;
    white-space: nowrap;
  }
  .person-role {
    position: absolute;
    left: 24px; top: 266px;
    color: var(--text-grey);
    font-size: 15px;
    line-height: 1.45;
    white-space: nowrap;
  }
  .contact-list { list-style: none; position: absolute; left: 0; right: 0; top: 330px; }
  .contact-row {
    display: flex; align-items: center;
    height: 52px;
    margin-bottom: 10px;
    background: var(--band-grey);
    padding-left: 16px;
  }
  .contact-icon { width: 30px; height: 30px; flex: none; margin-right: 16px; }
  .contact-text { color: var(--text-grey); font-size: 20px; white-space: nowrap; }
</style>
</head>
<body>

  <section class="card card--front" aria-label="Business card front">
    <div class="front-band">
      <div class="brand-name">Tbrite</div>
      <div class="brand-tagline">Professional Workplace Training Services</div>
    </div>
  </section>

  <section class="card card--back" aria-label="Business card back">
    <div class="back-logo-panel">
      <div class="brand-name">Tbrite</div>
      <div class="brand-tagline">Professional Workplace Training Services</div>
    </div>

    <div class="name-band"></div>
    <h1 class="person-name">Linda Marchbank</h1>
    <p class="person-role">Owner/Lead Trainer<br>Certified Coach &amp; Mentor Trainer</p>

    <ul class="contact-list">
      <li class="contact-row">
        <svg class="contact-icon" viewBox="0 0 30 30" aria-hidden="true">
          <rect x="9" y="3" width="12" height="24" rx="2.5" fill="none" stroke="#fff" stroke-width="2"/>
          <line x1="13" y1="23" x2="17" y2="23" stroke="#fff" stroke-width="2"/>
        </svg>
        <span class="contact-text">07853 416207</span>
      </li>
      <li class="contact-row">
        <svg class="contact-icon" viewBox="0 0 30 30" aria-hidden="true">
          <rect x="3" y="7" width="24" height="16" fill="#fff"/>
          <polyline points="3,7 15,17 27,7" fill="none" stroke="#d6d6d6" stroke-width="1.6"/>
        </svg>
        <span class="contact-text">lmarchbank@tbrite.co.uk</span>
      </li>
      <li class="contact-row">
        <svg class="contact-icon" viewBox="0 0 30 30" aria-hidden="true">
          <circle cx="15" cy="15" r="11" fill="none" stroke="#fff" stroke-width="2"/>
          <ellipse cx="15" cy="15" rx="5" ry="11" fill="none" stroke="#fff" stroke-width="1.6"/>
          <line x1="4" y1="15" x2="26" y2="15" stroke="#fff" stroke-width="1.6"/>
        </svg>
        <span class="contact-text">www.tbrite.co.uk</span>
      </li>
    </ul>
  </section>

</body>
</html>
```